Velora Aesthetica

Medical doctor providing aesthetic medicine

* Double sided card
* Logo to be on card
Other details:
* Dr. Mirela Kostvan, BSc, MBChB, CCFP
* #214-215, 27903 83 Ave, Surrey, BC, V2T 4K7
* 604-718-2943
* info@veloraclinic.ca
* www.veloraclinic.ca

Industry/Entity Type

Medical / Health & Beauty

Contact Information for Business Card

see 'Project Description'

Colors
0054AA
0677BA
7BADD7
CADEEF
E8F1F8
FFF300
FFF600
FEFA6F
FFFEC7
FFFEE8

Requirements
Must have
• Modern, high-end design

```html
<!DOCTYPE html>
<html lang="en">
<head>
<meta charset="utf-8">
<title>Velora Aesthetica – Business Card</title>
<link rel="stylesheet" href="https://fonts.googleapis.com/css2?family=Montserrat:wght@400;500;700&display=swap">
<style>
  :root {
    --navy: #233f5f;
    --gold: #dcb42a;
    --white: #ffffff;
    --backdrop: #e4e4e4;
  }
  * { margin: 0; padding: 0; box-sizing: border-box; }
  html, body {
    width: 1200px;
    height: 856px;
    overflow: hidden;
    background: var(--backdrop);
    font-family: "Montserrat", sans-serif;
  }
  .sheet {
    position: relative;
    width: 1200px;
    height: 856px;
    display: flex;
    align-items: center;
    justify-content: center;
    gap: 40px;
  }
  .card {
    position: relative;
    width: 540px;
    height: 309px;
    background: var(--navy);
    border-bottom: 4px solid var(--gold);
    border-left: 4px solid var(--gold);
    overflow: hidden;
  }

  /* Front side */
  .name-band {
    position: absolute;
    left: 0;
    top: 36px;
    width: 236px;
    height: 44px;
    background: var(--gold);
    padding: 7px 0 0 30px;
    color: var(--white);
  }
  .name-band .doctor-name {
    font-weight: 700;
    font-size: 13px;
    letter-spacing: 0.2px;
    text-transform: uppercase;
    line-height: 1.2;
  }
  .name-band .credentials {
    font-weight: 400;
    font-size: 10.5px;
    line-height: 1.35;
    padding-left: 14px;
  }
  .address {
    position: absolute;
    left: 92px;
    top: 112px;
    color: var(--white);
    font-size: 11px;
    line-height: 1.45;
  }
  .address .line-2 { padding-left: 14px; }
  .divider {
    position: absolute;
    left: 128px;
    top: 168px;
    width: 150px;
    height: 1.5px;
    background: var(--gold);
  }
  .contact-list {
    position: absolute;
    left: 150px;
    top: 184px;
    list-style: none;
    color: var(--white);
    font-size: 11px;
  }
  .contact-list li {
    display: flex;
    align-items: center;
    gap: 8px;
    height: 17px;
  }
  .contact-list li:nth-child(2) { padding-left: 10px; }
  .contact-list li:nth-child(3) { padding-left: 20px; }
  .contact-list svg { width: 11px; height: 11px; flex: none; }

  .brand {
    position: absolute;
    display: flex;
    align-items: center;
    color: var(--white);
    font-weight: 500;
    text-transform: uppercase;
  }
  .brand .brand-dot {
    border-radius: 50%;
    background: var(--gold);
    flex: none;
  }
  .front .brand {
    right: 38px;
    top: 118px;
    gap: 10px;
    font-size: 17px;
    letter-spacing: 4px;
    line-height: 1.3;
  }
  .front .brand .brand-dot { width: 12px; height: 12px; }

  /* Back side */
  .back {
    display: flex;
    align-items: center;
    justify-content: center;
  }
  .back .brand {
    position: static;
    gap: 14px;
    font-size: 28px;
    letter-spacing: 7px;
    line-height: 1.3;
  }
  .back .brand .brand-dot { width: 18px; height: 18px; }
</style>
</head>
<body>
<main class="sheet">

  <section class="card front" aria-label="Card front">
    <div class="name-band">
      <p class="doctor-name">Dr. Mirela Kostvan</p>
      <p class="credentials">BSc, MBChB, CCFP</p>
    </div>

    <address class="address">
      <div class="line-1">#214-215, 27903 83 Ave,</div>
      <div class="line-2">Surrey, BC, V2T 4K7</div>
    </address>

    <div class="divider"></div>

    <ul class="contact-list">
      <li>
        <svg viewBox="0 0 16 16" aria-hidden="true"><path fill="#dcb42a" d="M3.6 1.2l2.3 2.8-1.3 1.8c.9 2 2.5 3.7 4.6 4.6l1.8-1.3 2.8 2.3-1.3 2.7C7 13.7 2.3 9 .9 2.5z"/></svg>
        <span>604-718-2943</span>
      </li>
      <li>
        <svg viewBox="0 0 16 16" aria-hidden="true"><rect x="1" y="3" width="14" height="10" fill="#dcb42a"/><path d="M1.5 3.5L8 9l6.5-5.5" fill="none" stroke="#233f5f" stroke-width="1.3"/></svg>
        <span>info@veloraclinic.ca</span>
      </li>
      <li>
        <svg viewBox="0 0 16 16" aria-hidden="true"><circle cx="8" cy="8" r="7" fill="#dcb42a"/><path d="M1 8h14M8 1c-3 3.5-3 10.5 0 14M8 1c3 3.5 3 10.5 0 14" fill="none" stroke="#233f5f" stroke-width="1"/></svg>
        <span>www.veloraclinic.ca</span>
      </li>
    </ul>

    <div class="brand">
      <span class="brand-dot"></span>
      <span class="brand-name">Velora<br>Aesthetica</span>
    </div>
  </section>

  <section class="card back" aria-label="Card back">
    <div class="brand">
      <span class="brand-dot"></span>
      <span class="brand-name">Velora<br>Aesthetica</span>
    </div>
  </section>

</main>
</body>
</html>
```